Full page ad in a magazine

We would like an ad designed to be placed for advertising in magazines, theater playbills, etc. I have attached a copy of some previous ads that were done for us, although they need much improvement and redesigned. We have won "best chiropractor" awards that can be seen on our website home page at ferncliffspineandjoint.com

```html
<!DOCTYPE html>
<html lang="en">
<head>
<meta charset="utf-8">
<title>Ferncliff Spine &amp; Joint Center – Magazine Ad</title>
<link href="https://fonts.googleapis.com/css2?family=Exo+2:ital,wght@0,500;0,600;0,700;0,800;1,600&display=swap" rel="stylesheet">
<style>
  :root{
    --brand-red:#7d0000;
    --name-red:#8a0d0d;
    --accent-orange:#f6a21f;
    --ink:#1f1f1f;
    --footer:#2d2d2d;
    --white:#ffffff;
  }
  *{box-sizing:border-box;margin:0;padding:0}
  html,body{width:1200px;height:1200px;overflow:hidden;background:#fff}
  body{font-family:"Exo 2",sans-serif;color:var(--ink);position:relative}
  .ad-page{position:absolute;left:198px;top:96px;width:805px;height:1006px;background:var(--white);
    box-shadow:0 6px 18px rgba(0,0,0,.22);overflow:hidden}
  .ad-art{position:absolute;left:0;top:0;width:805px;height:1006px}

  .brand{position:absolute;left:60px;top:51px;display:flex;align-items:center;gap:14px}
  .brand-square{width:85px;height:95px;background:var(--brand-red)}
  .brand-name{color:var(--brand-red);font-weight:700;line-height:1.02;text-transform:uppercase}
  .brand-name .l1{display:block;font-size:24px;letter-spacing:10px}
  .brand-name .l2{display:block;font-size:42px;letter-spacing:1px}
  .brand-name .l3{display:block;font-size:24px;letter-spacing:28px}

  .doctor-photo{position:absolute;left:60px;top:196px;width:117px;height:140px;
    background:linear-gradient(160deg,#c9c4c0,#6e6a68);border:3px solid #fff;box-shadow:0 2px 6px rgba(0,0,0,.35)}
  .contact{position:absolute;left:199px;top:189px}
  .doctor-name{color:var(--name-red);font-size:28px;font-weight:700;line-height:1.1}
  .contact-row{display:flex;align-items:flex-start;gap:7px;font-weight:600;text-transform:uppercase}
  .contact-row svg{flex:none;margin-top:4px}
  .phone{font-size:22px;font-weight:700;margin-top:1px}
  .hours{font-size:14px;margin-top:8px}
  .location{font-size:17px;margin-top:9px;line-height:1.15}
  .location small{display:block;font-size:15px;text-transform:none;font-weight:700;line-height:1.15}

  .divider{position:absolute;left:528px;top:31px;width:1.5px;height:320px;background:#555}
  .awards{position:absolute;left:573px;top:34px;width:186px;text-align:center}
  .awards-title{font-weight:700;line-height:1}
  .awards-title .t1{display:block;font-size:21px}
  .awards-title .t2{display:block;font-size:22px;margin-top:2px}
  .awards-title .t3{display:block;font-size:14px;font-weight:600;margin-top:1px}
  .badges{position:absolute;left:573px;top:110px}

  .vote{position:absolute;left:110px;top:384px;width:341px;text-align:center;font-style:italic;font-weight:600;font-size:16px;line-height:1.3;color:var(--ink)}

  .headline{position:absolute;left:37px;top:536px;color:var(--white);font-weight:700;font-size:76px;line-height:67px;letter-spacing:-1px}
  .services{position:absolute;left:39px;top:686px;color:var(--white);font-weight:700;font-size:29px}
  .rule{position:absolute;left:40px;top:732px;width:44px;height:3px;background:var(--white)}
  .treating-label{position:absolute;left:39px;top:760px;color:var(--accent-orange);font-weight:700;font-size:35px}
  .conditions{position:absolute;left:40px;top:812px;display:grid;grid-template-columns:199px 170px;row-gap:8px;list-style:none}
  .conditions li{display:flex;align-items:center;gap:7px;color:var(--white);font-weight:700;font-size:25px;line-height:28px}

  .footer{position:absolute;left:0;top:959px;width:805px;height:47px;background:var(--footer);
    color:var(--white);font-size:21px;font-weight:600;letter-spacing:2.6px;text-align:center;line-height:47px}
</style>
</head>
<body>
<main class="ad-page">
  <svg class="ad-art" viewBox="0 0 805 1006">
    <defs>
      <linearGradient id="spineTone" x1="0" y1="0" x2="0" y2="1">
        <stop offset="0" stop-color="#f2f2f2"/>
        <stop offset=".6" stop-color="#cfcfcf"/>
        <stop offset="1" stop-color="#9c9c9c"/>
      </linearGradient>
      <linearGradient id="patientTone" x1="0" y1="0" x2="1" y2="1">
        <stop offset="0" stop-color="#b8b8b8"/>
        <stop offset=".55" stop-color="#8c8c8c"/>
        <stop offset="1" stop-color="#5c5c5c"/>
      </linearGradient>
    </defs>
    <path d="M0,432 C120,442 180,522 300,522 C450,522 560,382 805,360 L805,959 L0,959 Z" fill="var(--brand-red)"/>
    <ellipse cx="282" cy="424" rx="171" ry="84" fill="var(--accent-orange)"/>
    <path role="img" aria-label="Illustration of a human spine running across the page"
      d="M0,410 C120,420 180,500 300,500 C450,500 560,360 805,338" fill="none"
      stroke="url(#spineTone)" stroke-width="62"/>
    <path role="img" aria-label="Photo of a man seen from behind holding his neck and lower back in pain"
      d="M520,959 C470,900 420,840 415,790 C410,740 450,690 500,650 C520,560 545,500 610,472 C680,450 760,478 805,515 L805,959 Z"
      fill="url(#patientTone)"/>
  </svg>

  <div class="brand">
    <div class="brand-square"></div>
    <div class="brand-name"><span class="l1">Ferncliff</span><span class="l2">Spine &amp; Joint</span><span class="l3">Center</span></div>
  </div>

  <div class="doctor-photo" role="img" aria-label="Portrait photo of the chiropractor"></div>
  <div class="contact">
    <div class="doctor-name">Mark Ellison, DC</div>
    <div class="contact-row phone">
      <svg width="16" height="16" viewBox="0 0 24 24"><path fill="var(--name-red)" d="M6.6 10.8a15 15 0 0 0 6.6 6.6l2.2-2.2c.3-.3.7-.4 1-.2 1.1.4 2.3.6 3.6.6.6 0 1 .4 1 1V20c0 .6-.4 1-1 1A17 17 0 0 1 3 4c0-.6.4-1 1-1h3.5c.6 0 1 .4 1 1 0 1.3.2 2.5.6 3.6.1.3 0 .7-.2 1z"/></svg>
      555.214.7730
    </div>
    <div class="contact-row hours">
      <svg width="15" height="15" viewBox="0 0 24 24" fill="none" stroke="var(--name-red)" stroke-width="2"><rect x="3" y="5" width="18" height="16" rx="1"/><path d="M3 10h18M8 3v4M16 3v4"/></svg>
      Open Monday - Saturday
    </div>
    <div class="contact-row location">
      <svg width="12" height="16" viewBox="0 0 24 32"><path fill="var(--name-red)" d="M12 0C5.4 0 0 5.4 0 12c0 9 12 20 12 20s12-11 12-20C24 5.4 18.6 0 12 0zm0 17a5 5 0 1 1 0-10 5 5 0 0 1 0 10z"/></svg>
      <div>Ridgeview Location<small>1270 Alder Row, #104</small><small>Ferncliff, VA 20100</small></div>
    </div>
  </div>

  <div class="divider"></div>
  <div class="awards">
    <div class="awards-title"><span class="t1">BEST</span><span class="t2">CHIROPRACTOR</span><span class="t3">Awards</span></div>
  </div>
  <svg class="badges" width="190" height="170" viewBox="0 0 190 170" role="img" aria-label="Best chiropractor award badges">
    <circle cx="24" cy="25" r="24" fill="#222"/>
    <rect x="52" y="0" width="55" height="46" fill="#2d3fd1"/>
    <rect x="109" y="10" width="47" height="40" fill="#3a56d9"/>
    <ellipse cx="24" cy="74" rx="23" ry="10" fill="#d8d8d8"/>
    <rect x="52" y="60" width="57" height="33" fill="#1aa6e0"/>
    <circle cx="129" cy="75" r="16" fill="#222"/>
    <rect x="165" y="60" width="20" height="28" fill="#c8c8c8"/>
    <ellipse cx="24" cy="114" rx="23" ry="10" fill="#d8d8d8"/>
    <rect x="52" y="99" width="57" height="29" fill="#111"/>
    <circle cx="129" cy="113" r="16" fill="#222"/>
    <rect x="165" y="98" width="20" height="28" fill="#c8c8c8"/>
    <ellipse cx="24" cy="148" rx="23" ry="10" fill="#d8d8d8"/>
    <ellipse cx="80" cy="146" rx="24" ry="10" fill="#d8d8d8"/>
    <circle cx="129" cy="148" r="16" fill="#222"/>
    <rect x="165" y="133" width="20" height="28" fill="#c8c8c8"/>
  </svg>

  <div class="vote">Vote For us<br>www.coastalreaders.com/bestof</div>

  <h1 class="headline">NECK or<br>BACK PAIN?</h1>
  <div class="services">CHIROPRACTIC · MASSAGE</div>
  <div class="rule"></div>
  <div class="treating-label">Treating:</div>
  <ul class="conditions">
    <li><svg width="17" height="17" viewBox="0 0 20 20" fill="none" stroke="var(--accent-orange)" stroke-width="2"><rect x="2" y="3" width="15" height="15"/><path d="M6 10l3 3 8-9"/></svg>BACK PAIN</li>
    <li><svg width="17" height="17" viewBox="0 0 20 20" fill="none" stroke="var(--accent-orange)" stroke-width="2"><rect x="2" y="3" width="15" height="15"/><path d="M6 10l3 3 8-9"/></svg>JOINT PAIN</li>
    <li><svg width="17" height="17" viewBox="0 0 20 20" fill="none" stroke="var(--accent-orange)" stroke-width="2"><rect x="2" y="3" width="15" height="15"/><path d="M6 10l3 3 8-9"/></svg>NECK PAIN</li>
    <li><svg width="17" height="17" viewBox="0 0 20 20" fill="none" stroke="var(--accent-orange)" stroke-width="2"><rect x="2" y="3" width="15" height="15"/><path d="M6 10l3 3 8-9"/></svg>SCIATICA</li>
    <li><svg width="17" height="17" viewBox="0 0 20 20" fill="none" stroke="var(--accent-orange)" stroke-width="2"><rect x="2" y="3" width="15" height="15"/><path d="M6 10l3 3 8-9"/></svg>HEADACHES</li>
    <li><svg width="17" height="17" viewBox="0 0 20 20" fill="none" stroke="var(--accent-orange)" stroke-width="2"><rect x="2" y="3" width="15" height="15"/><path d="M6 10l3 3 8-9"/></svg>FATIGUE</li>
  </ul>

  <footer class="footer">www.FerncliffSpineAndJoint.com</footer>
</main>
</body>
</html>
```